Make attractive Packaging label for NUT BUTTERS jars

We at Velvet Orchard are launching our own line of NUT BUTTERS. We will be serving them in GLASS JARS ready packaged. I need attractive luxurious design for glass jar and should be designed ready to print.
I have attached glass jar pictures and measurement sheet.
My company logo has been attached. Also company details can be found on our facebook page.
product will be

ALMOND BUTTER
CASHEW BUTTER
PEANUT BUTTER
HAZELNUT BUTTER.

```html
<!DOCTYPE html>
<html lang="en">
<head>
<meta charset="utf-8">
<title>Velvet Orchard – Almond Butter Label</title>
<link rel="stylesheet" href="https://fonts.googleapis.com/css2?family=Bree+Serif&family=Quicksand:wght@500;700&display=swap">
<style>
  :root {
    --paper: #ede5da;
    --cocoa: #3b2a1f;
    --caramel: #c98a3c;
    --almond: #8a5232;
    --almond-light: #b5805a;
    --bowl: #f3f1ee;
    --butter: #c48c4c;
    --white: #ffffff;
  }
  * { margin: 0; padding: 0; box-sizing: border-box; }
  html, body { width: 1200px; height: 848px; overflow: hidden; background: var(--paper); }
  .label {
    position: relative;
    width: 1200px;
    height: 848px;
    background: var(--paper);
    overflow: hidden;
    font-family: "Quicksand", sans-serif;
    color: var(--cocoa);
  }
  .photo { position: absolute; }
  .photo--bowl {
    left: -40px; top: -40px; width: 317px; height: 308px;
    border-radius: 50%;
    background: radial-gradient(circle at 45% 45%, var(--butter) 0 52%, var(--bowl) 56% 100%);
  }
  .photo--almonds-left {
    left: -30px; top: 250px; width: 330px; height: 240px;
    border-radius: 45%;
    background: radial-gradient(ellipse at 35% 50%, var(--almond) 0%, rgba(138,82,50,0.55) 45%, rgba(237,229,218,0) 72%);
  }
  .photo--almonds-top {
    left: 760px; top: -20px; width: 440px; height: 320px;
    border-radius: 45%;
    background: radial-gradient(ellipse at 60% 35%, rgba(138,82,50,0.7) 0%, rgba(181,128,90,0.35) 45%, rgba(237,229,218,0) 72%);
  }
  .photo--almonds-bottom {
    left: 840px; top: 480px; width: 380px; height: 380px;
    border-radius: 45%;
    background: radial-gradient(ellipse at 55% 55%, rgba(138,82,50,0.7) 0%, rgba(181,128,90,0.35) 45%, rgba(237,229,218,0) 72%);
  }
  .brand {
    position: absolute;
    left: 370px; top: 60px; width: 470px;
    text-align: center;
    font-family: "Quicksand", sans-serif;
    font-weight: 700;
    font-size: 104px;
    line-height: 0.98;
    letter-spacing: -2px;
    color: var(--caramel);
  }
  .product-badge {
    position: absolute;
    left: 346px; top: 369px; width: 503px; height: 296px;
    border-radius: 50%;
    background: var(--cocoa);
  }
  .product-name {
    position: absolute;
    left: 346px; top: 430px; width: 452px;
    text-align: center;
    font-family: "Bree Serif", serif;
    font-weight: 400;
    font-size: 104px;
    line-height: 82px;
    color: var(--white);
  }
  .contact {
    position: absolute;
    left: 150px; top: 684px; width: 900px;
    text-align: center;
  }
  .contact__phone {
    font-weight: 700;
    font-size: 40px;
    line-height: 46px;
    letter-spacing: 0.5px;
    margin-bottom: 6px;
  }
  .contact__line {
    display: flex;
    justify-content: center;
    align-items: center;
    gap: 12px;
    font-weight: 500;
    font-size: 25px;
    line-height: 29px;
    letter-spacing: 0.3px;
  }
  .contact__line svg { flex: none; }
</style>
</head>
<body>
  <main class="label">
    <div class="photo photo--bowl" role="img" aria-label="Photo of a white bowl filled with creamy almond butter"></div>
    <div class="photo photo--almonds-left" role="img" aria-label="Photo of scattered whole almonds"></div>
    <div class="photo photo--almonds-top" role="img" aria-label="Photo of scattered whole almonds"></div>
    <div class="photo photo--almonds-bottom" role="img" aria-label="Photo of scattered whole almonds"></div>

    <h1 class="brand">Velvet<br>Orchard</h1>

    <div class="product-badge" role="img" aria-label="Dark brown almond-shaped badge illustration"></div>
    <h2 class="product-name">Almond<br>Butter</h2>

    <section class="contact">
      <p class="contact__phone">+353 87 402 7718</p>
      <p class="contact__line">
        <svg width="18" height="13" viewBox="0 0 18 13" aria-hidden="true"><rect x="0.5" y="0.5" width="17" height="12" fill="var(--caramel)"/><path d="M1 1 L9 7 L17 1" fill="none" stroke="var(--paper)" stroke-width="1.4"/></svg>
        hello@velvetorchard.ie
      </p>
      <p class="contact__line">
        <svg width="16" height="16" viewBox="0 0 16 16" aria-hidden="true"><rect width="16" height="16" rx="3" fill="var(--caramel)"/></svg>
        www.velvetorchard.ie/community
      </p>
      <p class="contact__line">
        <svg width="22" height="20" viewBox="0 0 22 20" aria-hidden="true"><path d="M11 2 C7.5 2 5.5 4.5 5.5 7.3 C5.5 10.5 11 15 11 15 C11 15 16.5 10.5 16.5 7.3 C16.5 4.5 14.5 2 11 2 Z" fill="none" stroke="var(--caramel)" stroke-width="1.8"/><circle cx="11" cy="7.3" r="2" fill="var(--caramel)"/><path d="M4 12 L1 19 L21 19 L18 12" fill="none" stroke="var(--caramel)" stroke-width="1.8" stroke-linejoin="round"/></svg>
        Linden Market Hall, 14 Linden Row, Dublin, Ireland
      </p>
    </section>
  </main>
</body>
</html>
```